KettleMint.com Cooking Spice Jar Label Design

I need the following labels designed.

dimensions in inches. Drawings attached and logo attached

a. 3.5 oz wrap around spice label 2.3" tall x 3.3" wide
b. 5.5 oz warp around spice label 3.3" tall x 3.6" wide
c. 32 oz clear bottle. Flat label
c. flat label. 2.25 x 4
d. flat front of bottle label 5 x 3.5

Target Market(s)

gourmet cooks. restaurant managers. chefs. grocery store owners.

Industry/Entity Type

Cooking

Font styles to use
Other font styles liked:
• see attached logo

Requirements
Must have
• must be elegant and sophisticated using the existing logo attached.
• please look at www.kettlemint.com to see what the 3.5 oz label looks like today with the old logo.
Nice to have

```html
<!DOCTYPE html>
<html lang="en">
<head>
<meta charset="utf-8">
<title>KettleMint Adobo Labels</title>
<link rel="stylesheet" href="https://fonts.googleapis.com/css2?family=Libre+Baskerville:wght@400;700&display=swap">
<style>
  :root {
    --backdrop: #2f2a22;
    --paper: #efe9d3;
    --paper-edge: #e2dabd;
    --swirl: #e6dcc0;
    --ink: #3b2f24;
    --seal-green: #24614a;
    --seal-face: #f3eedd;
    --band: #d9da9c;
    --band-rule: #7a5a2e;
    --band-ink: #5a4a34;
  }
  * { box-sizing: border-box; margin: 0; padding: 0; }
  html, body {
    width: 1200px;
    height: 871px;
    overflow: hidden;
  }
  body {
    background: var(--backdrop);
    font-family: "Libre Baskerville", Georgia, serif;
    color: var(--ink);
    position: relative;
  }
  .label {
    position: absolute;
    background: var(--paper);
    border-radius: 0.6em;
    overflow: hidden;
  }
  .label--32oz  { left: 130px; top: 150px; width: 340px; height: 570px; font-size: 16px; }
  .label--5oz   { left: 560px; top: 300px; width: 260px; height: 420px; font-size: 12.4px; }
  .label--3oz   { left: 900px; top: 370px; width: 220px; height: 350px; font-size: 10.5px; }

  .swirl-field {
    position: absolute;
    inset: 0;
    background:
      radial-gradient(circle at 15% 60%, var(--swirl) 0 18%, transparent 19%),
      radial-gradient(circle at 88% 45%, var(--swirl) 0 14%, transparent 15%),
      radial-gradient(circle at 20% 95%, var(--swirl) 0 16%, transparent 17%),
      radial-gradient(circle at 85% 92%, var(--swirl) 0 14%, transparent 15%),
      linear-gradient(180deg, var(--paper) 0%, var(--paper-edge) 100%);
    opacity: 0.8;
  }
  .brand {
    position: absolute;
    top: 27%;
    left: 0;
    right: 0;
    display: flex;
    align-items: center;
    justify-content: center;
    gap: 0.4em;
    transform: translateY(-50%);
  }
  .brand__dot {
    width: 0.9em;
    height: 0.9em;
    border-radius: 50%;
    background: var(--seal-green);
  }
  .brand__name {
    font-size: 2.1em;
    font-weight: 400;
    color: var(--ink);
    letter-spacing: 0.01em;
  }
  .seal {
    position: absolute;
    top: 60%;
    left: 50%;
    width: 7.4em;
    height: 7.4em;
    transform: translate(-50%, -50%);
    border-radius: 50%;
    background: var(--seal-face);
    border: 0.55em solid var(--seal-green);
    box-shadow: 0 0 0 0.15em var(--seal-face), 0 0 0 0.28em var(--seal-green);
    display: flex;
    align-items: center;
    justify-content: center;
    z-index: 2;
  }
  .seal__name {
    font-weight: 700;
    font-size: 1.35em;
    color: var(--ink);
  }
  .band {
    position: absolute;
    top: 72%;
    left: 0;
    right: 0;
    height: 11%;
    background: var(--band);
    border-top: 0.14em solid var(--band-rule);
    border-bottom: 0.14em solid var(--band-rule);
    display: flex;
    flex-direction: column;
    align-items: center;
    justify-content: center;
    text-align: center;
    color: var(--band-ink);
    font-size: 0.88em;
    line-height: 1.35;
  }
  .size {
    position: absolute;
    top: 90%;
    left: 0;
    right: 0;
    text-align: center;
    font-size: 0.85em;
    color: var(--band-ink);
  }
</style>
</head>
<body>

  <section class="label label--32oz">
    <div class="swirl-field" role="img" aria-label="Faint cream swirl pattern across the label"></div>
    <div class="brand"><span class="brand__dot"></span><span class="brand__name">KettleMint</span></div>
    <div class="seal"><span class="seal__name">Adobo</span></div>
    <div class="band"><span>all purpose seasoning</span><span>used in Caribbean cooking</span></div>
    <div class="size">32oz</div>
  </section>

  <section class="label label--5oz">
    <div class="swirl-field" role="img" aria-label="Faint cream swirl pattern across the label"></div>
    <div class="brand"><span class="brand__dot"></span><span class="brand__name">KettleMint</span></div>
    <div class="seal"><span class="seal__name">Adobo</span></div>
    <div class="band"><span>all purpose seasoning</span><span>used in Caribbean cooking</span></div>
    <div class="size">5.5oz</div>
  </section>

  <section class="label label--3oz">
    <div class="swirl-field" role="img" aria-label="Faint cream swirl pattern across the label"></div>
    <div class="brand"><span class="brand__dot"></span><span class="brand__name">KettleMint</span></div>
    <div class="seal"><span class="seal__name">Adobo</span></div>
    <div class="band"><span>all purpose seasoning</span><span>used in Caribbean cooking</span></div>
    <div class="size">3.5oz</div>
  </section>

</body>
</html>
```